New solo practice law firm is looking for an elegant, professional, and interactive web design

I need a web design and developer for a new small law firm in a river city, California called Dorian Kessly Law, A Professional Corporation. I am a trial lawyer who represents average people facing difficult litigation disputes, including criminal defense as a former prosecutor and civil litigation as a civil litigator. Criminal defense includes domestic violence, battery, assault, drug possession, theft, DUI, etc. Civil litigation includes business disputes, property disputes, employment disputes, family law disputes, and immigration issues. I would like to see web designs that incorporate my logo and use the logo's navy blue and gold colors. I have uploaded the files of my logo to this brief. Please only use the navy blue and gold version. Overall, I want the design to look firm, professional, and elegant.

I plan on having the following pages on my website: (1) Home, (2) Dorian Kessly, (3) Practice Areas, (4) Insights, (5) Contact. I've hand drawn a preliminary sketch concept of what I envision the home page's layout to look like (attached with a text version). I would like your design to keep a similar layout for the homepage and incorporate my logo's colors within it but I am open to creative layout alternatives/ideas. I would like the other pages to have a similar look and feel as the home page. Some of the areas currently in my sketch do not have the full text. You can insert other text for now and I will provide the winner the full text.

In terms of the pictures on the website, I enjoy images of courthouses, columns (example attached but I cannot use this one), and, if possible, images from a river city, CA in my background (headshot attached). A plus would be live images that move and also sections of the webpage moving in the viewers view as they scroll down on the page. Also, it would be great to have my logo act as the tab for the website. I can provide other versions of the logo if needed.

I look forward to seeing your Wordpress designs!

People needing legal representation.

Law

Coded - Design and coding required

5+ page

Serif

• Incorporate my logo and my logo's colors.
• Live pictures and images appearing as viewers scroll on page.

```html
<!DOCTYPE html>
<html lang="en">
<head>
<meta charset="utf-8">
<title>Dorian Kessly Law</title>
<link href="https://fonts.googleapis.com/css2?family=Poppins:wght@300;400;500&family=Playfair+Display:wght@700&display=swap" rel="stylesheet">
<style>
  :root{
    --navy:#14213a;
    --navy-deep:#0f1a2e;
    --navy-soft:#2b3c5e;
    --gold:#b59a62;
    --gold-dark:#8c7242;
    --gold-light:#d6bf8a;
    --ink:#3a3f4a;
    --white:#ffffff;
  }
  *{margin:0;padding:0;box-sizing:border-box}
  html,body{width:678px;height:1200px;overflow:hidden;background:var(--white)}
  body{font-family:'Poppins',sans-serif;color:var(--ink);position:relative}

  .top-bar{position:absolute;left:0;top:0;width:678px;height:22px;background:var(--navy-deep);color:var(--white);font-size:7px;display:flex;align-items:center;justify-content:space-between;padding:0 50px;z-index:3}
  .top-bar .address{display:flex;align-items:center;gap:5px}
  .top-bar .lang{font-weight:500}

  .hero{position:absolute;left:0;top:22px;width:678px;height:270px;background:linear-gradient(180deg,#2a3652 0%,#23324f 45%,#1b2a48 100%);z-index:1}
  .hero-scene{position:absolute;inset:0;background:radial-gradient(ellipse at 50% 60%,rgba(70,90,130,.55),rgba(20,30,55,0) 70%)}
  .hero-cut{position:absolute;left:0;bottom:0;width:678px;height:52px}
  .brand{position:absolute;display:flex;align-items:center;gap:8px}
  .brand-mark{width:14px;height:14px;border:1.5px solid var(--gold);flex:none}
  .brand-name{color:var(--gold);font-weight:400;letter-spacing:2.5px;line-height:1.35}
  .brand-name span{display:block}
  .header-brand{left:222px;top:19px}
  .header-brand .brand-name{font-size:11.5px}
  .header-brand .brand-name span+span{font-size:5.6px;letter-spacing:2px;text-align:center}
  .cta{position:absolute;left:507px;top:17px;width:112px;height:27px;border:1.5px solid var(--gold);color:var(--white);font-size:6.6px;line-height:1.15;padding:5px 8px;display:flex;justify-content:space-between;align-items:center}
  .cta small{display:block;font-size:6.4px;color:#d9d9e3}
  .cta b{font-weight:500}
  .main-nav{position:absolute;top:64px;left:0;width:678px;display:flex;justify-content:center;gap:19px;font-size:8.4px;font-weight:500;color:var(--white)}
  .main-nav .active{color:var(--gold)}
  .hero-title{position:absolute;top:113px;left:0;width:678px;text-align:center;font-size:40px;font-weight:500;color:var(--gold);letter-spacing:-.5px}

  .about{position:absolute;left:0;top:300px;width:678px;height:430px}
  .about-eyebrow{position:absolute;left:49px;top:118px;font-size:26px;font-weight:400;color:var(--gold);letter-spacing:.3px}
  .about-title{position:absolute;left:47px;top:146px;font-size:45px;font-weight:400;color:var(--navy);letter-spacing:.5px}
  .about-copy{position:absolute;left:50px;top:205px;width:302px;font-size:9px;line-height:14px;color:var(--ink)}
  .about-panel{position:absolute;left:551px;top:67px;width:127px;height:355px;background:linear-gradient(160deg,var(--navy-soft),#1d2c4c)}
  .about-frame{position:absolute;left:371px;top:224px;width:212px;height:174px;border:3px solid var(--gold-light);border-top:none;border-right-color:var(--gold)}
  .about-frame-top{position:absolute;left:371px;top:224px;width:14px;height:3px;background:var(--gold-light)}
  .portrait{position:absolute;left:386px;top:96px;width:241px;height:290px;background:linear-gradient(135deg,#a98a52 0%,#8a6d3c 40%,#2a2622 60%,#1c1a18 100%)}

  .quote{position:absolute;left:0;top:745px;width:678px;text-align:center}
  .quote-mark{font-family:'Playfair Display',serif;font-size:86px;line-height:58px;height:44px;overflow:hidden;color:var(--gold);font-weight:700}
  .quote-text{width:420px;margin:2px auto 0;font-size:9.5px;line-height:14px;color:var(--ink)}

  .footer{position:absolute;left:0;top:872px;width:678px;height:328px}
  .footer-cut{position:absolute;left:0;top:0;width:678px;height:328px}
  .footer-brand{left:50px;top:140px}
  .footer-brand .brand-name{font-size:11.5px}
  .footer-brand .brand-name span+span{font-size:5.6px;letter-spacing:2px;text-align:center}
  .footer-map{position:absolute;left:275px;top:110px;width:180px;height:110px;background:radial-gradient(ellipse,rgba(255,255,255,.06),rgba(255,255,255,0) 70%)}
  .footer-heading{font-size:10px;font-weight:400;color:var(--gold);letter-spacing:.4px;margin-bottom:9px}
  .contact-info{position:absolute;left:327px;top:114px;color:var(--white);font-size:7.2px;line-height:9px}
  .contact-info li{list-style:none;display:flex;gap:5px;margin-bottom:3px}
  .contact-info svg{flex:none;margin-top:1px}
  .social{display:flex;gap:4px;margin-top:10px}
  .social span{width:20px;height:20px;background:var(--navy-deep)}
  .quick-links{position:absolute;left:508px;top:114px;color:var(--white);font-size:7.2px}
  .quick-links li{list-style:none;margin-bottom:4.4px}
  .quick-links li::before{content:"›";color:var(--gold);margin-right:4px}
  .footer-rule{position:absolute;left:50px;top:258px;width:575px;height:1px;background:rgba(255,255,255,.2)}
  .to-top{position:absolute;left:638px;top:246px;width:24px;height:24px;background:var(--gold);display:flex;align-items:center;justify-content:center}
  .disclaimer{position:absolute;left:0;top:278px;width:678px;text-align:center;color:#d8dbe3;font-size:7px;line-height:10px}
  .copyright{position:absolute;left:0;top:300px;width:678px;text-align:center;color:var(--white);font-size:8px;font-weight:500}
</style>
</head>
<body>

<div class="top-bar">
  <div class="address">
    <svg width="5" height="7" viewBox="0 0 10 14"><path d="M5 0a5 5 0 0 0-5 5c0 4 5 9 5 9s5-5 5-9a5 5 0 0 0-5-5zm0 7a2 2 0 1 1 0-4 2 2 0 0 1 0 4z" fill="#b59a62"/></svg>
    2710 harbor ridge rd suite # 204 cedar hollow ca 90000
  </div>
  <div class="lang">EN ⌄</div>
</div>

<header class="hero">
  <div class="hero-scene" role="img" aria-label="Evening city skyline along a river"></div>
  <div class="brand header-brand">
    <div class="brand-mark"></div>
    <div class="brand-name"><span>DORIAN KESSLY LAW</span><span>A PROFESSIONAL CORPORATION</span></div>
  </div>
  <div class="cta"><div><small>REQUEST A</small><b>FREE CONSULTATION</b></div><span>›</span></div>
  <nav class="main-nav">
    <span>HOME</span><span class="active">DORIAN KESSLY</span><span>PRACTICE AREAS</span><span>INSIGHTS</span><span>CONTACT</span>
  </nav>
  <h1 class="hero-title">DORIAN KESSLY</h1>
  <svg class="hero-cut" viewBox="0 0 678 52" preserveAspectRatio="none"><polygon points="0,52 678,0 678,52" fill="#ffffff"/><polygon points="640,3 678,0 678,2" fill="#9aa3b5"/></svg>
</header>

<section class="about">
  <div class="about-panel"></div>
  <div class="about-frame"></div>
  <div class="about-frame-top"></div>
  <div class="portrait" role="img" aria-label="Portrait of Dorian Kessly in a dark suit in front of a courthouse library interior"></div>
  <p class="about-eyebrow">READY, RELIABLE, AND</p>
  <h2 class="about-title">EXPERIENCED</h2>
  <p class="about-copy">Dorian Kessly joined Harlow Vance’ litigation team after serving as Deputy District Attorney in the Marlow County District Attorney’s Office. Shortly after starting with the D.A.’s Office, he was entrusted to serve as lead trial attorney in over a dozen cases, working diligently as a progressive prosecutor to find resolutions that served justice for victims, defendants, and the community. When alternative solutions were exhausted, he took cases to trial and had an overwhelmingly favorable conviction record in the cases he tried. His background in litigation also includes internships at the State Attorney General’s Office, Riverbend County District Attorney’s Office, and in private practice as an employment litigator.</p>
</section>

<section class="quote">
  <div class="quote-mark">“</div>
  <p class="quote-text">I apply my background as a progressive prosecutor and as an employment litigator to now represent business and real estate clients in complex litigation. I search for creative resolutions to business disputes, but stand ready with an impressive trial record.</p>
</section>

<footer class="footer">
  <svg class="footer-cut" viewBox="0 0 678 328" preserveAspectRatio="none"><polygon points="0,53 678,0 678,328 0,328" fill="#14213a"/></svg>
  <div class="footer-map" role="img" aria-label="Faint dotted world map"></div>
  <div class="brand footer-brand">
    <div class="brand-mark"></div>
    <div class="brand-name"><span>DORIAN KESSLY LAW</span><span>A PROFESSIONAL CORPORATION</span></div>
  </div>
  <div class="contact-info">
    <h3 class="footer-heading">CONTACT INFO</h3>
    <ul>
      <li><svg width="6" height="8" viewBox="0 0 10 14"><path d="M5 0a5 5 0 0 0-5 5c0 4 5 9 5 9s5-5 5-9a5 5 0 0 0-5-5zm0 7a2 2 0 1 1 0-4 2 2 0 0 1 0 4z" fill="#b59a62"/></svg><span>2710 HARBOR RIDGE RD<br>SUITE # 204<br>CEDAR HOLLOW CA 90000</span></li>
      <li><svg width="7" height="7" viewBox="0 0 12 12"><path d="M2.5 0l2 3-1.2 1.3a7 7 0 0 0 4.4 4.4L9 7.5l3 2-1 2.5C5 12 0 7 0 1z" fill="#b59a62"/></svg><span>( 555 ) 310-0142</span></li>
      <li><svg width="7" height="6" viewBox="0 0 12 9"><rect width="12" height="9" fill="#b59a62"/><path d="M0 0l6 5 6-5" stroke="#14213a" fill="none"/></svg><span>dorian@doriankesslylaw.com</span></li>
    </ul>
    <div class="social"><span></span><span></span><span></span></div>
  </div>
  <div class="quick-links">
    <h3 class="footer-heading">QUICK LINKS</h3>
    <ul>
      <li>Home</li><li>Dorian Kessly</li><li>Practice Areas</li><li>Insights</li><li>Contact</li><li>Privacy Policy</li>
    </ul>
  </div>
  <div class="footer-rule"></div>
  <div class="to-top"><svg width="8" height="11" viewBox="0 0 8 11"><path d="M4 11V1M1 4l3-3 3 3" stroke="#fff" fill="none"/></svg></div>
  <p class="disclaimer">The information on this website is for general information purposes only. nothing on this site should be taken as<br>legal advice for any individual case or situation, constitute an attorney - client relationship</p>
  <p class="copyright">© Copyright 2021 All Rights Reserved</p>
</footer>

</body>
</html>
```